FULL Stationary & Business Cards for Innovative Software Company
Stationary/Business Card/Email Signatures
FULL Stationary & Business Cards for Innovative Software Company - Software
Creative Brief
Professional
Miles Tenvard
Managing Partner
412 Harrow Bend Road Suite 309, North Annex Mississauga, ON L4T 2K8
milest@quelvoworks.example
www.quelvoworks.example
restwzeasy restwzeasy
Please submit all of your final stationary designs. We are making a decision soon.
sevensky sevensky
Please tell which design no we use to make stationary package??
Can you please submit full stationary for the designs that were evaluated with stars?
Watermark logo on back of the card is very interesting.
The cards must show all of the provided contact information. Some of the designs only show the telephone without the address.
The front of the card should be easy to read, but also be interesting. All white on the front is little boring.
We like the designs with the back of the card in red instead of blue.
We are not very interested in a border on the front of the card.
Check #140, also its a veiled contest, no one can see other designs, so kindly send a comment/feedback through private messeging service of panelhive, thanks! regards
design #132, looks better, but little plain on the front page.
We like the designs with some creative content on the front, but not too intrusive. We are not very interested in all white front of the card - we feel that is too plan. At the same time, the design should complement the information, not distract from it. Please continue to submit your designs. Innovative, fresh, professional are some of the characteristics we are trying to communicate.
On the folder designs, please be little more creative. A lot of them look plain. We are trying to communicate that we are an interesting, innovative, leading edge software company.
#81, the content is all in the centre of the card. Please try to spread the content around the card.
We like the back designs with only the logo instead of having the contact information.
We like the designs that make use of the space instead of all of the text being grouped in one specific area of the card leaving 1/2 of the business card space obviously empty. It should be easy for someone to quickly scan the card and see the name, address, and contact information instead of having to search for it.
We like the red back of the card better than the blue.
Please use the Quelvo logo without the "TM" (trademark).
Xpert Xpert
Sir, can you give some star rating first then we move towards stationery to the rated designs. Thanks
Thank you for the designs, but please keep in mind that the request is for all stationary including 2 sided business cards, letterhead, envelopes, email signature, and portfolio.

```html
<!DOCTYPE html>
<html lang="en">
<head>
<meta charset="utf-8">
<title>Quelvo Business Card</title>
<link href="https://fonts.googleapis.com/css2?family=Open+Sans:wght@400;600;700;800&display=swap" rel="stylesheet">
<style>
  :root {
    --backdrop: #d9dbde;
    --brand-blue: #3d86d6;
    --brand-blue-dark: #2f6fb8;
    --brand-red: #b9262f;
    --paper: #ffffff;
    --ink: #3b3f45;
    --ink-soft: #6a6f76;
  }
  * { margin: 0; padding: 0; box-sizing: border-box; }
  html, body {
    width: 1200px; height: 653px; overflow: hidden;
    background: var(--backdrop);
    font-family: "Open Sans", Arial, sans-serif;
  }
  .stage {
    position: relative; width: 1200px; height: 653px;
    display: flex; align-items: center; justify-content: center; gap: 60px;
  }
  .card {
    position: relative; width: 500px; height: 286px; overflow: hidden;
    box-shadow: 0 8px 22px rgba(0,0,0,0.18);
  }
  .card-back {
    background: var(--brand-blue);
    display: flex; align-items: center; justify-content: center;
  }
  .wordmark {
    font-weight: 800; color: var(--brand-red); letter-spacing: 1px;
    line-height: 1;
  }
  .card-back .wordmark { font-size: 64px; }
  .card-front { background: var(--paper); }
  .card-front .swoosh { position: absolute; inset: 0; }
  .card-front .wordmark {
    position: absolute; left: 124px; top: 92px; font-size: 38px;
  }
  .identity {
    position: absolute; left: 34px; bottom: 28px; color: var(--paper);
  }
  .identity .name {
    font-size: 15px; font-weight: 700; text-transform: uppercase; letter-spacing: 0.6px;
  }
  .identity .role { font-size: 10.5px; opacity: 0.85; margin-top: 2px; }
  .contact {
    position: absolute; right: 22px; top: 40px; width: 180px;
    text-align: right; color: var(--ink); font-size: 8.5px; line-height: 1.45;
    list-style: none;
  }
  .contact li { display: flex; justify-content: flex-end; align-items: center; gap: 6px; }
  .contact .address { display: block; margin-bottom: 6px; color: var(--ink-soft); }
  .contact .icon { width: 8px; height: 8px; flex: none; }
</style>
</head>
<body>
<main class="stage">
  <section class="card card-back" aria-label="Card back">
    <span class="wordmark">Quelvo</span>
  </section>

  <section class="card card-front" aria-label="Card front">
    <svg class="swoosh" viewBox="0 0 500 286" preserveAspectRatio="none" aria-hidden="true">
      <path d="M0 286 L0 140 C60 70 200 35 330 55 C220 62 110 80 80 140 C85 195 250 222 500 210 L500 286 Z" fill="var(--brand-blue)"/>
      <path d="M80 140 C85 195 250 222 500 210" fill="none" stroke="var(--brand-blue-dark)" stroke-width="3"/>
      <path d="M0 140 C60 70 200 35 330 55" fill="none" stroke="var(--brand-red)" stroke-width="7"/>
    </svg>
    <span class="wordmark">Quelvo</span>

    <ul class="contact">
      <li class="address">412 Harrow Bend Road Suite 309,<br>North Annex Mississauga,<br>ON L4T 2K8</li>
      <li>T 905 555 0142
        <svg class="icon" viewBox="0 0 10 10"><path d="M2 1 L4 1 L5 3 L4 4 C4.5 5.5 5 6 6 6.5 L7 5.5 L9 6.5 L9 8.5 C5 9 1 5 2 1 Z" fill="var(--brand-blue)"/></svg></li>
      <li>F 905 555 0143
        <svg class="icon" viewBox="0 0 10 10"><rect x="1" y="2" width="8" height="6" rx="1" fill="var(--brand-blue)"/></svg></li>
      <li>M 416 555 0178
        <svg class="icon" viewBox="0 0 10 10"><rect x="3" y="1" width="4" height="8" rx="1" fill="var(--brand-blue)"/></svg></li>
      <li>milest@quelvoworks.example
        <svg class="icon" viewBox="0 0 10 10"><rect x="1" y="2" width="8" height="6" fill="none" stroke="var(--brand-blue)"/><path d="M1 2 L5 5.5 L9 2" fill="none" stroke="var(--brand-blue)"/></svg></li>
      <li>www.quelvoworks.example
        <svg class="icon" viewBox="0 0 10 10"><circle cx="5" cy="5" r="4" fill="none" stroke="var(--brand-blue)"/><path d="M1 5 H9 M5 1 V9" stroke="var(--brand-blue)"/></svg></li>
    </ul>

    <div class="identity">
      <p class="name">Miles Tenvard</p>
      <p class="role">Managing Partner</p>
    </div>
  </section>
</main>
</body>
</html>
```